Corrowin Sack operates across the US and Australasia providing calico bags to small business through to large enterprise across all verticals. Our bags are the most premium in the market place and our customer service is second to none. Our competitive advantage lays in our competitive pricing, superior quality and outstanding customer service.

Industry/Entity Type

Business

Contact Information for Business Card

Corrowin Sack
Marisol Quenby
Managing Director
marisol@corrowinsack.com
www.corrowinsack.com.au
Mobile:- 0471 896 305
Level 3, 284 Harwick Street
Melbourne Victoria Australia 3000

```html
<!DOCTYPE html>
<html lang="en">
<head>
<meta charset="utf-8">
<title>Corrowin Sack — Business Card</title>
<link rel="stylesheet" href="https://fonts.googleapis.com/css2?family=Tinos:ital,wght@0,400;0,700;1,400&display=swap">
<style>
  :root {
    --brand-green: #73b63a;
    --paper-white: #ffffff;
    --ink-black: #161616;
  }
  html, body {
    margin: 0;
    padding: 0;
    overflow: hidden;
    background: var(--paper-white);
  }
  .card {
    position: relative;
    width: 1200px;
    height: 740px;
    overflow: hidden;
    background: var(--brand-green);
    font-family: "Tinos", "Times New Roman", serif;
  }
  .card__panel {
    position: absolute;
    inset: 0;
    width: 1200px;
    height: 740px;
  }
  .card__panel-fill {
    fill: var(--paper-white);
  }
  .brand-name {
    position: absolute;
    right: 98px;
    top: 92px;
    margin: 0;
    font-size: 74px;
    font-weight: 700;
    line-height: 1;
    letter-spacing: -1px;
    color: var(--paper-white);
    white-space: nowrap;
  }
  .contact,
  .address {
    position: absolute;
    right: 98px;
    margin: 0;
    text-align: right;
    color: var(--paper-white);
    font-size: 40px;
    line-height: 46px;
    letter-spacing: -1.2px;
    font-style: normal;
  }
  .contact { top: 226px; }
  .address { top: 412px; }
  .contact__line,
  .address__line {
    display: block;
    white-space: nowrap;
  }
  .person {
    position: absolute;
    left: 96px;
    top: 502px;
    color: var(--ink-black);
  }
  .person__name {
    margin: 0;
    font-size: 40px;
    font-weight: 700;
    line-height: 48px;
    letter-spacing: -1.2px;
  }
  .person__role {
    margin: 0;
    font-size: 40px;
    font-style: italic;
    line-height: 48px;
    letter-spacing: -1px;
  }
</style>
</head>
<body>
  <main class="card">
    <svg class="card__panel" viewBox="0 0 1200 740" aria-hidden="true">
      <path class="card__panel-fill" d="M0 0 H300 C120 210, 560 420, 420 740 H0 Z"/>
    </svg>

    <h1 class="brand-name">CORROWIN SACK</h1>

    <p class="contact">
      <span class="contact__line">marisol@corrowinsack.com</span>
      <span class="contact__line">www.corrowinsack.com.au</span>
      <span class="contact__line">Mobile:- 0471 896 305</span>
    </p>

    <address class="address">
      <span class="address__line">Level 3,</span>
      <span class="address__line">284 Harwick Street</span>
      <span class="address__line">Melbourne Victoria</span>
      <span class="address__line">Australia 3000</span>
    </address>

    <div class="person">
      <p class="person__name">Marisol Quenby</p>
      <p class="person__role">Managing Director</p>
    </div>
  </main>
</body>
</html>
```